Electrician Letterhead Design BLR

We need some letterhead for our bills and other papers.
Customer address is on the right side (Swiss format)
A4 format

Design should also be applicable on Cards

Target Market(s)

Private Customers, Small Business

Industry/Entity Type

Electrician

Other font styles liked:
• incised 901

Colors
00AB8E
00BBA5
67D7C9
C6EFE9
E9F9F6

```html
<!DOCTYPE html>
<html lang="de">
<head>
<meta charset="utf-8">
<title>BLR Letterhead</title>
<link href="https://fonts.googleapis.com/css2?family=Roboto:wght@400;500;900&display=swap" rel="stylesheet">
<style>
  :root {
    --brand: #10a594;
    --brand-pale: #d6e6e3;
    --ink: #1a1a1a;
    --paper: #ffffff;
  }
  * { box-sizing: border-box; margin: 0; padding: 0; }
  html, body {
    width: 1200px; height: 1000px; overflow: hidden;
    background: var(--paper);
    font-family: "Roboto", Arial, sans-serif;
  }
  .canvas { position: relative; width: 1200px; height: 1000px; }
  .sheet {
    position: absolute; left: 280px; top: 0; width: 640px; height: 952px;
    background: var(--paper); overflow: hidden;
  }
  .brand { position: absolute; left: 58px; top: 68px; }
  .brand-name {
    display: flex; align-items: center; gap: 10px;
    font-weight: 900; font-size: 56px; line-height: 1; color: var(--brand);
    letter-spacing: 1px;
  }
  .brand-dot { width: 14px; height: 14px; background: var(--brand); border-radius: 50%; }
  .brand-sub {
    margin-top: 6px; font-size: 10px; font-weight: 500; color: var(--ink);
    letter-spacing: 0.2px;
  }
  .contact {
    position: absolute; left: 486px; top: 80px;
    border-left: 2px solid var(--brand); padding-left: 7px;
    font-size: 11px; line-height: 13.5px; color: var(--ink);
  }
  .contact-line { display: flex; align-items: center; gap: 5px; }
  .contact-line svg { width: 9px; height: 9px; fill: var(--brand); flex: none; }
  .corner-block {
    position: absolute; left: 266px; top: 849px; width: 374px; height: 103px;
    background: var(--brand-pale);
  }
  .footer-band {
    position: absolute; left: 0; top: 890px; width: 640px; height: 30px;
    background: var(--brand); color: #fff;
    display: flex; align-items: center; justify-content: center;
    font-size: 17px; letter-spacing: 0.3px;
  }
</style>
</head>
<body>
<div class="canvas">
  <div class="sheet">
    <header>
      <div class="brand">
        <div class="brand-name">BLR <span class="brand-dot"></span></div>
        <div class="brand-sub">Elektrotechnik Brandl GmbH</div>
      </div>
      <address class="contact" style="font-style:normal">
        <div class="contact-line">
          <svg viewBox="0 0 10 10" aria-hidden="true"><path d="M1 3c0-1.2 1.5-2 4-2s4 .8 4 2L7.5 4 6.5 2.8h-3L2.5 4zM2.5 5h5l1 4h-7z"/></svg>
          +41 44 000 00 00
        </div>
        <div class="contact-line">
          <svg viewBox="0 0 10 10" aria-hidden="true"><circle cx="5" cy="5" r="4.2" fill="none" stroke="#10a594" stroke-width="1.1"/><path d="M1 5h8M5 1c-2 2.4-2 5.6 0 8M5 1c2 2.4 2 5.6 0 8" fill="none" stroke="#10a594" stroke-width=".9"/></svg>
          www.blr-elektro.ch
        </div>
        <div class="contact-line">
          <svg viewBox="0 0 10 10" aria-hidden="true"><path d="M0.5 2h9v6h-9z"/><path d="M0.5 2.3 5 5.6l4.5-3.3" fill="none" stroke="#fff" stroke-width=".9"/></svg>
          info@blr-elektro.ch
        </div>
      </address>
    </header>
    <div class="corner-block" aria-hidden="true"></div>
    <footer class="footer-band">www.blr-elektro.ch</footer>
  </div>
</div>
</body>
</html>
```